RTB sticker for the back window of a car

Well this design is for the back of our car. We want it to be plain and simple but stand out. I have put something together which is a bit to plain and i would like to to look a little bit different. Possibly have a picture of a shipping container on it so people know what we are trying to sell? I don't need our logo on there but i want the phone number and email. Thank you in advance.

Requirements
Must have
• The phone number 0452 317 906 not the one in the picture please.
• Also must have the email that IS in the picture please.
Nice to have
• A picture of a shipping container so people know what we are talking about.

```html
<!DOCTYPE html>
<html lang="en">
<head>
<meta charset="utf-8">
<title>RTB – Shipping Containers for Sale window sticker</title>
<link rel="stylesheet" href="https://fonts.googleapis.com/css2?family=Roboto+Condensed:wght@700&family=Archivo+Black&display=swap">
<style>
  :root {
    --page-bg: #e9e9e9;
    --brand-red: #b3192f;
    --deep-red: #7e0f1f;
    --mid-red: #9a1426;
    --sand: #ddd5c9;
    --sand-light: #eee9e1;
    --white: #ffffff;
  }
  html, body {
    margin: 0;
    padding: 0;
    width: 1200px;
    height: 999px;
    overflow: hidden;
    background: var(--page-bg);
  }
  .canvas {
    width: 1200px;
    height: 999px;
    display: flex;
    align-items: center;
    justify-content: center;
  }
  .window-sticker {
    width: 1160px;
    height: 424px;
    display: block;
  }
  .headline {
    font-family: "Roboto Condensed", "Arial Narrow", sans-serif;
    font-weight: 700;
    fill: var(--brand-red);
  }
  .headline-sale {
    font-family: "Archivo Black", "Arial Black", sans-serif;
    fill: var(--brand-red);
  }
  .contact {
    font-family: "Roboto Condensed", "Arial Narrow", sans-serif;
    font-weight: 700;
    fill: var(--brand-red);
  }
</style>
</head>
<body>
<main class="canvas">
  <svg class="window-sticker" viewBox="0 0 930 340" xmlns="http://www.w3.org/2000/svg" aria-label="RTB shipping containers for sale window sticker">
    <defs>
      <linearGradient id="sand-fade" x1="0" y1="0" x2="1" y2="0">
        <stop offset="0" stop-color="var(--sand)"/>
        <stop offset="0.5" stop-color="var(--sand-light)"/>
        <stop offset="1" stop-color="var(--sand)"/>
      </linearGradient>
      <linearGradient id="red-fade" x1="0" y1="0" x2="1" y2="0">
        <stop offset="0" stop-color="var(--brand-red)"/>
        <stop offset="1" stop-color="var(--mid-red)"/>
      </linearGradient>
      <clipPath id="window-shape">
        <path d="M40 6 Q45 0 70 0 L860 0 Q885 0 890 6 L928 250 Q932 330 900 336 L30 336 Q-2 330 2 250 Z"/>
      </clipPath>
    </defs>

    <g clip-path="url(#window-shape)">
      <!-- sand upper field -->
      <rect class="sand-field" x="0" y="0" width="930" height="340" fill="url(#sand-fade)"/>
      <!-- red lower waves -->
      <path class="red-wave" d="M0 250 C180 210 330 300 520 285 C690 272 820 215 930 185 L930 340 L0 340 Z" fill="url(#red-fade)"/>
      <path class="white-sweep" d="M0 250 C180 210 330 300 520 285 C690 272 820 215 930 185 L930 205 C820 235 690 292 520 300 C330 312 180 232 0 268 Z" fill="var(--white)"/>
      <path class="deep-wave" d="M120 340 C260 290 420 300 560 318 C700 336 820 300 930 250 L930 340 Z" fill="var(--deep-red)"/>
      <path class="mid-wave" d="M0 300 C90 286 170 300 230 340 L0 340 Z" fill="var(--mid-red)"/>
    </g>

    <text class="headline" x="90" y="76" font-size="50" textLength="505" lengthAdjust="spacingAndGlyphs">SHIPPING CONTAINERS</text>
    <text class="headline" x="162" y="158" font-size="44">for</text>
    <text class="headline-sale" x="242" y="160" font-size="92" textLength="272" lengthAdjust="spacingAndGlyphs">SALE</text>

    <rect class="container-art" x="600" y="42" width="255" height="92" fill="var(--brand-red)" role="img" aria-label="Illustration of a shipping container"/>

    <text class="contact contact-phone" x="545" y="190" font-size="40" textLength="316" lengthAdjust="spacingAndGlyphs">Ph: 0452 317 906</text>
    <text class="contact contact-email" x="545" y="224" font-size="22" textLength="312" lengthAdjust="spacingAndGlyphs">Email: sales@rtbcm.com.au</text>
  </svg>
</main>
</body>
</html>
```